Korrin Baptiste Law website for a law firm

modern clean website for a small boutique law firm. Based in Sacramento, CA and the Bay Area. Practice areas of Family Law, Civil litigation, and Criminal Defense. We already have a logo design as well as attorney pictures to include on page.
Would like images of California included on site.
Would like site to go with Logo that is already designed...blue/grey/white colors.

Industry/Entity Type

Law Firm

Number of Pages Required

5+ page

Requirements
Must have
• I already have several pages of content drafted. Just need the pages with images to input content. Must be clean and modern feel. Want it to reflect California and small boutique feel that is provided personalized legal attention.
• Must have a page where I can blog or post articles on.

```html
<!DOCTYPE html>
<html lang="en">
<head>
<meta charset="utf-8">
<title>Korrin Baptiste Law</title>
<link href="https://fonts.googleapis.com/css2?family=Open+Sans:wght@400;600;700&family=Playfair+Display:wght@400&display=swap" rel="stylesheet">
<style>
:root{
  --navy:#1f3268;
  --blue:#2f6fb8;
  --blue-deep:#2c4f8f;
  --accent-red:#d42020;
  --white:#ffffff;
  --footer:#9c9c9c;
  --field:#c9c9c9;
  --ink:#1b1b1b;
}
*{margin:0;padding:0;box-sizing:border-box}
html,body{width:773px;height:1200px;overflow:hidden;background:var(--white)}
body{position:relative;font-family:'Open Sans',sans-serif}
.site{position:relative;width:773px;height:1200px;overflow:hidden}

/* header */
.header{position:absolute;left:0;top:0;width:773px;height:89px;background:var(--white)}
.phone{position:absolute;left:612px;top:0;display:flex;align-items:center;gap:6px;color:var(--accent-red);font-weight:600;font-size:11.5px}
.brand{position:absolute;left:16px;top:28px;font-size:31px;font-weight:400;color:var(--blue);letter-spacing:1px;line-height:1}
.nav{position:absolute;left:360px;top:48px;display:flex;align-items:center;font-size:11.5px;font-weight:600;color:var(--blue)}
.nav a{color:var(--blue);text-decoration:none}
.nav a.current{color:var(--navy)}
.nav .sep{margin:0 13px;color:var(--blue)}

/* hero */
.hero{position:absolute;left:0;top:89px;width:773px;height:383px;
  background:radial-gradient(ellipse at 50% 35%,#8a8a88 0%,#55514d 45%,#2a2522 80%),#3a3330}
.hero::after{content:"";position:absolute;left:0;bottom:0;width:100%;height:95px;background:linear-gradient(#5a3f2c,#3b2719)}
.hero-content{position:absolute;left:0;top:0;width:100%;height:100%;z-index:1;text-align:center;color:var(--white);font-family:'Playfair Display',serif}
.hero-title{position:absolute;left:0;right:0;top:96px;font-size:35px;font-weight:400;letter-spacing:.5px}
.hero-tagline{position:absolute;left:0;right:0;top:172px;font-size:24px;font-weight:400}
.btn-outline{position:absolute;left:313px;top:230px;width:145px;height:28px;border:1.5px solid var(--white);color:var(--white);font-family:'Open Sans',sans-serif;font-size:12px;letter-spacing:2px;display:flex;align-items:center;justify-content:center}

/* intro */
.intro{position:absolute;left:0;top:472px;width:773px;height:171px;text-align:center;color:var(--blue-deep)}
.intro-heading{position:absolute;left:0;right:0;top:48px;font-size:15px;font-weight:600}
.intro-text{position:absolute;left:214px;width:343px;top:81px;font-size:11.3px;font-weight:600;line-height:14.6px;text-align:justify;text-align-last:center}

/* practice areas */
.practice{position:absolute;left:0;top:643px;width:773px;height:370px;
  background:linear-gradient(180deg,#8fa1b3 0%,#8d9aa4 30%,#6e8a8e 55%,#5b7a5a 80%,#6b7a48 100%)}
.practice-title{position:absolute;left:0;right:0;top:57px;padding-left:0;text-align:center;margin-left:38px;font-size:23px;font-weight:700;color:var(--blue-deep);letter-spacing:1px}
.area{position:absolute;width:160px;text-align:center}
.area-name{font-size:14px;font-weight:700;color:var(--ink);white-space:nowrap}
.area-icon{position:absolute;width:73px;height:73px;background:rgba(255,255,255,.85);border-radius:6px}
.area-btn{position:absolute;width:90px;height:25px;border:1.5px solid var(--white);color:var(--white);font-size:8.5px;display:flex;align-items:center;justify-content:center}

/* footer */
.footer{position:absolute;left:0;top:1013px;width:773px;height:187px;background:var(--footer);color:var(--white)}
.footer-links{position:absolute;left:67px;top:33px;height:103px;border-left:1px solid var(--white);padding-left:14px;list-style:none}
.footer-links li{font-size:9px;height:23.3px}
.help-title{position:absolute;left:209px;top:39px;font-size:11.5px;font-weight:700}
.field{position:absolute;background:var(--field);border:1px solid #d8d8d8;font-size:5px;color:#777;padding:3px 5px}
.send{position:absolute;left:460px;top:129px;width:110px;height:19px;border:1px solid #cfcfcf;font-size:8px;color:#dadada;display:flex;align-items:center;justify-content:center;letter-spacing:.5px}
.connect{position:absolute;left:675px;top:36px;font-size:11.5px;font-weight:700}
.social{position:absolute;left:678px;top:56px;display:flex;gap:7px}
.social span{width:11px;height:11px;border-radius:50%;background:var(--ink)}
</style>
</head>
<body>
<div class="site">
  <header class="header">
    <div class="phone">
      <svg width="13" height="13" viewBox="0 0 14 14" aria-hidden="true"><circle cx="7" cy="7" r="6.3" fill="none" stroke="#555" stroke-width="1"/><path d="M4.6 3.8c.4-.3.8-.3 1 .1l.6 1.1c.2.3 0 .6-.2.8l-.3.3c.3.8.9 1.4 1.7 1.7l.3-.3c.2-.2.5-.4.8-.2l1.1.6c.4.2.4.6.1 1-.5.6-1.1.9-1.8.7-1.9-.6-3.2-1.9-3.8-3.8-.2-.7.1-1.3.5-2z" fill="#555"/></svg>
      123-456-7890
    </div>
    <div class="brand">KBLAW</div>
    <nav class="nav">
      <a class="current">HOME</a><span class="sep">|</span>
      <a>ABOUT</a><span class="sep">|</span>
      <a>PRACTICE AREAS</a><span class="sep">|</span>
      <a>CONTACT</a><span class="sep">|</span>
      <a>BLOG</a>
    </nav>
  </header>

  <section class="hero" role="img" aria-label="Photo of a hand holding a wooden judge's gavel above a sound block on a wooden desk">
    <div class="hero-content">
      <h1 class="hero-title">KORRIN BAPTISTE LAW</h1>
      <p class="hero-tagline">Strong reputations don’t go unnoticed.</p>
      <div class="btn-outline">Learn About Us</div>
    </div>
  </section>

  <section class="intro">
    <h2 class="intro-heading">A well-respected boutique law firm in Northern California</h2>
    <p class="intro-text">We specialize in Business Law, Family Law and Criminal Defense. Our goal is to provide our clients with the best possible outcome in each and every case.</p>
  </section>

  <section class="practice" role="img" aria-label="Photo of the Golden Gate Bridge seen from green coastal cliffs above the bay">
    <h2 class="practice-title">PRACTICE AREAS</h2>

    <div class="area" style="left:30px;top:139px"><div class="area-name">FAMILY LAW</div></div>
    <div class="area-icon" role="img" aria-label="Family icon" style="left:77px;top:177px"></div>
    <div class="area-btn" style="left:66px;top:273px">Know more</div>

    <div class="area" style="left:302px;top:133px"><div class="area-name">BUSINESS LAW</div></div>
    <div class="area-icon" role="img" aria-label="Handshake icon" style="left:347px;top:177px"></div>
    <div class="area-btn" style="left:334px;top:274px">Know more</div>

    <div class="area" style="left:576px;top:133px"><div class="area-name">CRIMINAL DEFENSE</div></div>
    <div class="area-icon" role="img" aria-label="Person behind bars icon" style="left:621px;top:177px"></div>
    <div class="area-btn" style="left:613px;top:273px">Know more</div>
  </section>

  <footer class="footer">
    <ul class="footer-links">
      <li>Home</li><li>About Us</li><li>Contact Us</li><li>Practice Areas</li><li>Blog</li>
    </ul>
    <div class="help-title">Looking for Help?</div>
    <div class="field" style="left:333px;top:32px;width:110px;height:17px">Your name</div>
    <div class="field" style="left:333px;top:63px;width:110px;height:18px">Your Email Address</div>
    <div class="field" style="left:333px;top:96px;width:110px;height:18px">Your phone no.</div>
    <div class="field" style="left:460px;top:31px;width:110px;height:83px">Your message</div>
    <div class="send">SEND</div>
    <div class="connect">CONNECT</div>
    <div class="social" aria-label="Social links"><span></span><span></span><span></span></div>
  </footer>
</div>
</body>
</html>
```